Baby Shower Invitation for Vectored Image Provided

Caroline & Desmond's Baby Shower - Black/White/Gold Colors preferred
Please use the vectored portrait image attached. I'd like us on the lower right side of the invitation.
Can be horizontal or vertical layout.
The second image attached has the information needed for you to complete.
I don't want that style copied, it is just an example.

```html
<!DOCTYPE html>
<html lang="en">
<head>
<meta charset="utf-8">
<title>Caroline &amp; Desmond's Baby Shower Invitation</title>
<link rel="stylesheet" href="https://fonts.googleapis.com/css2?family=Dancing+Script:wght@700&family=Lilita+One&family=Courier+Prime:wght@400;700&family=Patrick+Hand&display=swap">
<style>
  :root {
    --ink: #111111;
    --paper: #ffffff;
    --backdrop: #eeeeee;
    --gold: #f2b70f;
    --gold-deep: #d99a06;
    --gold-pale: #fbe9a8;
    --cream: #fffbea;
    --grey-text: #3a3a3a;
    --photo-dark: #2b2624;
    --photo-mid: #6b5a50;
  }
  * { margin: 0; padding: 0; box-sizing: border-box; }
  html, body { width: 870px; height: 1200px; overflow: hidden; background: var(--backdrop); }
  .sheet { position: relative; width: 870px; height: 1200px; }

  .card { position: absolute; top: 306px; width: 420px; height: 588px; overflow: hidden; }
  .card-front {
    left: 10px;
    background: repeating-linear-gradient(to bottom, var(--ink) 0 13px, var(--paper) 13px 26px);
  }
  .card-back { left: 440px; background: var(--paper); }

  .info-panel {
    position: absolute;
    left: 46px; top: 28px;
    width: 328px; height: 300px;
    background: var(--paper);
    text-align: center;
    font-family: "Courier Prime", monospace;
    color: var(--ink);
  }
  .title-baby {
    font-family: "Dancing Script", cursive;
    font-size: 30px; color: var(--gold);
    line-height: 1; margin-top: 16px;
  }
  .title-row { display: flex; justify-content: center; align-items: center; gap: 6px; }
  .title-shower {
    font-family: "Lilita One", sans-serif;
    font-size: 30px; font-weight: 400; color: var(--gold);
    letter-spacing: 1px; line-height: 1;
  }
  .footprints { width: 20px; height: 24px; }
  .invite-line { font-size: 8.5px; margin-top: 8px; }
  .couple-names {
    font-family: "Dancing Script", cursive;
    font-size: 17px; color: var(--gold-deep);
    margin-top: 4px; white-space: nowrap;
  }
  .when-row {
    display: grid;
    grid-template-columns: 1fr 70px 1fr;
    align-items: center;
    margin: 14px 28px 0;
    font-size: 11px;
  }
  .when-row .cell { border-top: 1px solid var(--ink); border-bottom: 1px solid var(--ink); padding: 5px 0; }
  .when-row .cell p + p { margin-top: 3px; font-size: 9px; }
  .mustache-small { width: 52px; height: 18px; margin: 0 auto; display: block; }
  .details-row {
    display: grid;
    grid-template-columns: 1fr 70px 1fr;
    margin: 22px 28px 0;
    font-size: 9px; line-height: 1.5;
    text-align: left; white-space: nowrap;
  }
  .details-row strong { font-weight: 700; }
  .portrait {
    position: absolute;
    left: 150px; top: 300px;
    width: 150px; height: 288px;
    background: linear-gradient(to bottom, var(--photo-mid), var(--photo-dark));
    border-radius: 70px 70px 0 0;
  }

  .back-pattern {
    position: absolute; inset: 0;
    background: radial-gradient(circle at 50% 50%, var(--cream) 0 30%, var(--gold-pale) 100%);
  }
  .greeting {
    position: absolute;
    left: 0; right: 0; top: 226px;
    text-align: center;
    font-family: "Patrick Hand", cursive;
    font-size: 40px; line-height: 1.05;
    color: var(--grey-text);
    letter-spacing: 1px;
  }
  .mustache-large { position: absolute; left: 130px; top: 318px; width: 160px; height: 54px; }
</style>
</head>
<body>
  <svg width="0" height="0" style="position:absolute" aria-hidden="true">
    <symbol id="mustache-shape" viewBox="0 0 120 40">
      <path d="M60 14 C50 2 30 2 20 14 C14 22 6 24 0 18 C4 32 20 38 36 32 C46 28 54 24 60 20 C66 24 74 28 84 32 C100 38 116 32 120 18 C114 24 106 22 100 14 C90 2 70 2 60 14 Z" fill="var(--ink)"/>
    </symbol>
  </svg>
  <main class="sheet">
    <article class="card card-front">
      <section class="info-panel">
        <p class="title-baby">Baby</p>
        <div class="title-row">
          <h1 class="title-shower">SHOWER</h1>
          <svg class="footprints" role="img" aria-label="Baby footprints illustration" viewBox="0 0 20 24">
            <rect x="0" y="0" width="20" height="24" rx="8" fill="var(--gold)"/>
          </svg>
        </div>
        <p class="invite-line">Please join us for a Baby Shower honoring</p>
        <h2 class="couple-names">Caroline &amp; Desmond's Baby Shower</h2>
        <div class="when-row">
          <div class="cell"><p>saturday</p><p>11:00 am</p></div>
          <svg class="mustache-small" viewBox="0 0 120 40" aria-hidden="true"><use href="#mustache-shape"/></svg>
          <div class="cell"><p>september</p><p>14</p></div>
        </div>
        <div class="details-row">
          <p class="venue">The Linden Hall<br>2019 Maple Ridge Rd<br>Cary, NC</p>
          <span></span>
          <p class="rsvp"><strong>RSVP</strong> to Desmond<br>at 555-014-2267<br>by August 10th</p>
        </div>
      </section>
      <div class="portrait" role="img" aria-label="Portrait of the expecting couple"></div>
    </article>

    <article class="card card-back">
      <div class="back-pattern" role="img" aria-label="Pattern of yellow baby clothes, bottles and stars"></div>
      <h2 class="greeting">HELLO BABY<br>BOY</h2>
      <svg class="mustache-large" viewBox="0 0 120 40" aria-hidden="true"><use href="#mustache-shape"/></svg>
    </article>
  </main>
</body>
</html>
```